Bref créative
Stationary for telecom company
KLV Telecommunications
Professional
Dinh Quoc Bao
Director
47 Hoa Lu Street, Ward 5, Go Vap District, Ho Chi Minh City
bao.dinh@mrq.net.vn
www.klvtelecom.vn

```html
<!DOCTYPE html>
<html lang="en">
<head>
<meta charset="utf-8">
<title>KLV Telecommunications – Business Cards</title>
<link rel="stylesheet" href="https://fonts.googleapis.com/css2?family=Roboto:wght@400;700;900&display=swap">
<style>
  :root {
    --page-bg: #e6e8eb;
    --card-white: #ffffff;
    --card-white-shade: #eef0f3;
    --card-clear: rgba(236, 240, 245, 0.78);
    --card-clear-shade: rgba(214, 221, 230, 0.78);
    --brand-blue: #2459a6;
    --band-blue: #1f4f96;
    --band-blue-light: #3a6db5;
    --band-blue-dark: #173f7c;
    --silver: #cfd6df;
    --text-white: #ffffff;
    --text-dark: #2b2f36;
    --card-edge: rgba(0, 0, 0, 0.12);
  }
  * { box-sizing: border-box; margin: 0; padding: 0; }
  html, body { width: 1200px; height: 730px; overflow: hidden; }
  body {
    background: var(--page-bg);
    font-family: "Roboto", Arial, sans-serif;
    position: relative;
  }
  .card {
    position: absolute;
    width: 488px;
    height: 258px;
    border-radius: 16px;
    overflow: hidden;
    border: 1px solid var(--card-edge);
    box-shadow: 0 6px 18px rgba(0, 0, 0, 0.18);
  }
  .card--white { background: linear-gradient(180deg, var(--card-white) 0%, var(--card-white-shade) 50%); }
  .card--clear { background: linear-gradient(180deg, var(--card-clear) 0%, var(--card-clear-shade) 55%); }
  .card--front.card--white { left: 77px; top: 66px; }
  .card--front.card--clear { left: 638px; top: 66px; }
  .card--back.card--white { left: 77px; top: 392px; }
  .card--back.card--clear { left: 638px; top: 392px; }

  .wordmark {
    position: absolute;
    left: 0; right: 0;
    text-align: center;
    color: var(--brand-blue);
    font-weight: 900;
    line-height: 1;
  }
  .wordmark__name { display: block; font-size: 46px; letter-spacing: 1px; }
  .wordmark__sub { display: block; font-size: 13px; letter-spacing: 1.2px; margin-top: 3px; }
  .card--front .wordmark { top: 40px; }
  .card--back .wordmark { top: 54px; }
  .card--back.card--clear .wordmark { opacity: 0.32; }

  .band {
    position: absolute;
    left: 0; right: 0;
    background: linear-gradient(180deg, var(--band-blue-light) 0%, var(--band-blue) 45%, var(--band-blue-dark) 100%);
    border-top: 4px solid var(--silver);
  }
  .card--front .band { top: 132px; height: 64px; }
  .card--back .band { top: 150px; bottom: 0; }
  .card--back.card--clear .band { opacity: 0.88; }

  .name-line {
    position: absolute;
    top: 14px; left: 0; right: 0;
    text-align: center;
    color: var(--text-white);
    font-size: 14px;
    font-weight: 700;
  }
  .name-line__role { font-weight: 400; }
  .name-line__rule {
    display: inline-block; width: 1px; height: 13px;
    background: var(--text-white); margin: 0 6px; vertical-align: -2px;
  }

  .contacts {
    position: absolute;
    left: 26px; right: 20px;
    top: 208px;
    color: var(--text-dark);
    font-size: 8.5px;
    line-height: 16px;
  }
  .contacts__row { display: flex; gap: 14px; white-space: nowrap; }
  .contact { display: inline-flex; align-items: center; gap: 4px; }
  .contact svg { width: 10px; height: 10px; flex: none; }

  .web {
    position: absolute;
    left: 0; right: 0; bottom: 30px;
    text-align: center;
    color: var(--text-white);
    font-size: 11px;
    letter-spacing: 3px;
  }
</style>
</head>
<body>

<svg width="0" height="0" style="position:absolute" aria-hidden="true">
  <defs>
    <symbol id="icon-pin" viewBox="0 0 10 10"><circle cx="5" cy="5" r="5" fill="#2459a6"/><path d="M5 2.2a1.8 1.8 0 0 1 1.8 1.8C6.8 5.4 5 7.8 5 7.8S3.2 5.4 3.2 4A1.8 1.8 0 0 1 5 2.2z" fill="#fff"/></symbol>
    <symbol id="icon-phone" viewBox="0 0 10 10"><circle cx="5" cy="5" r="5" fill="#2459a6"/><path d="M3.3 2.5l1 1-.5.8a4 4 0 0 0 1.9 1.9l.8-.5 1 1-.6.8C5.2 7.3 2.7 4.8 2.5 3.1z" fill="#fff"/></symbol>
    <symbol id="icon-mail" viewBox="0 0 10 10"><circle cx="5" cy="5" r="5" fill="#2459a6"/><rect x="2.6" y="3.3" width="4.8" height="3.4" fill="#fff"/><path d="M2.6 3.3L5 5.2l2.4-1.9" stroke="#2459a6" stroke-width=".5" fill="none"/></symbol>
    <symbol id="icon-web" viewBox="0 0 10 10"><circle cx="5" cy="5" r="5" fill="#2459a6"/><circle cx="5" cy="5" r="2.5" stroke="#fff" stroke-width=".6" fill="none"/><path d="M2.5 5h5M5 2.5v5" stroke="#fff" stroke-width=".5"/></symbol>
  </defs>
</svg>

<!-- Front, white -->
<section class="card card--front card--white">
  <div class="wordmark"><span class="wordmark__name">KLV</span><span class="wordmark__sub">TELECOMMUNICATIONS</span></div>
  <div class="band">
    <p class="name-line">Dinh Quoc Bao<span class="name-line__rule"></span><span class="name-line__role">Director</span></p>
  </div>
  <div class="contacts">
    <div class="contacts__row">
      <span class="contact"><svg><use href="#icon-pin"/></svg>47 Hoa Lu Street, Ward 5, Go Vap District, Ho Chi Minh City</span>
      <span class="contact"><svg><use href="#icon-phone"/></svg>(84) 8 39 274816</span>
    </div>
    <div class="contacts__row">
      <span class="contact"><svg><use href="#icon-phone"/></svg>(84) 8 39 612057</span>
      <span class="contact"><svg><use href="#icon-mail"/></svg>bao.dinh@mrq.net.vn</span>
      <span class="contact"><svg><use href="#icon-web"/></svg>www.klvtelecom.vn</span>
    </div>
  </div>
</section>

<!-- Front, clear -->
<section class="card card--front card--clear">
  <div class="wordmark"><span class="wordmark__name">KLV</span><span class="wordmark__sub">TELECOMMUNICATIONS</span></div>
  <div class="band">
    <p class="name-line">Dinh Quoc Bao<span class="name-line__rule"></span><span class="name-line__role">Director</span></p>
  </div>
  <div class="contacts">
    <div class="contacts__row">
      <span class="contact"><svg><use href="#icon-pin"/></svg>47 Hoa Lu Street, Ward 5, Go Vap District, Ho Chi Minh City</span>
      <span class="contact"><svg><use href="#icon-phone"/></svg>(84) 8 39 274816</span>
    </div>
    <div class="contacts__row">
      <span class="contact"><svg><use href="#icon-phone"/></svg>(84) 8 39 612057</span>
      <span class="contact"><svg><use href="#icon-mail"/></svg>bao.dinh@mrq.net.vn</span>
      <span class="contact"><svg><use href="#icon-web"/></svg>www.klvtelecom.vn</span>
    </div>
  </div>
</section>

<!-- Back, white -->
<section class="card card--back card--white">
  <div class="wordmark"><span class="wordmark__name">KLV</span><span class="wordmark__sub">TELECOMMUNICATIONS</span></div>
  <div class="band"></div>
  <p class="web">www.klvtelecom.vn</p>
</section>

<!-- Back, clear -->
<section class="card card--back card--clear">
  <div class="wordmark"><span class="wordmark__name">KLV</span><span class="wordmark__sub">TELECOMMUNICATIONS</span></div>
  <div class="band"></div>
  <p class="web">www.klvtelecom.vn</p>
</section>

</body>
</html>
```